Flyer Design Project for a Seminar "Charting The Handover"

KTMW Chartered Accountants would like a flyer invitation designed for our upcoming seminar "Charting The Handover." The invitation should be created in MS Word, for editing capabilities on our end.

Seminar Title: "Charting The Handover: Securing and Growing Worth Across An Ownership Shift"

This is a complimentary breakfast seminar for Owners and CEOs of private corporations with revenues ranging from $2M to $150M.

Please leave substantial room to enter overview information on the seminar and topics of discussion.

We are open to bold colours and interesting graphics.

An example of a very amateur in-house design is attached.

Target Market(s)

Business owners and CEOs (typically men between 40 and 50 years old)

Industry/Entity Type

Business

Requirements
Must have
• -Substantial space to enter overview info about the seminar
-Space to enter logistical info about the seminar (i.e When, Where and RSVP info)
-Text should be Gill Sans. 1 page only
Should not have
• Stock photos of fake office people or American dollars (we are a Canadian company)!

```html
<!DOCTYPE html>
<html lang="en">
<head>
<meta charset="utf-8">
<title>Charting The Handover – Breakfast Seminar</title>
<link href="https://fonts.googleapis.com/css2?family=Cabin:wght@400;600;700&display=swap" rel="stylesheet">
<style>
  :root {
    --paper: #ffffff;
    --ink: #111111;
    --headline-red: #e0241b;
    --gold: #c9a227;
    --date-brown: #8a6a1c;
    --orange: #e5731c;
    --panel-top: #f7ebc2;
    --panel-bottom: #e6cf8c;
    --panel-edge: #c9b072;
    --tab: #8c8c8c;
    --rule-brown: #9b6b3a;
    --sky-top: #9fc0de;
    --sky-bottom: #f2f5f8;
    --brand-navy: #1d3c6e;
  }
  * { box-sizing: border-box; margin: 0; padding: 0; }
  html, body { width: 1200px; height: 935px; overflow: hidden; background: var(--paper); }
  .flyer {
    position: relative; width: 1200px; height: 935px; overflow: hidden;
    background: var(--paper); color: var(--ink);
    font-family: "Gill Sans", "Gill Sans MT", "Cabin", sans-serif; text-transform: uppercase;
  }
  .masthead { position: absolute; left: 60px; top: 50px; width: 760px; text-align: center; }
  .masthead__title {
    font-weight: 700; font-size: 34px; letter-spacing: 6px;
    color: var(--paper); -webkit-text-stroke: 1.3px var(--headline-red);
    text-shadow: 0 0 3px rgba(224,36,27,.5);
  }
  .masthead__subtitle {
    margin-top: 10px; font-weight: 700;
    font-size: 20px; line-height: 24px; letter-spacing: 3px; color: var(--gold);
    text-shadow: 1px 1px 1px rgba(0,0,0,.35);
  }
  .masthead__audience { margin-top: 16px; font-size: 16px; line-height: 21px; letter-spacing: 2px; font-weight: 600; }
  .masthead__date { margin-top: 18px; font-size: 15px; line-height: 17px; letter-spacing: 1.5px; color: var(--date-brown); font-weight: 700; }
  .hero-image {
    position: absolute; left: 871px; top: 45px; width: 203px; height: 220px;
    background: linear-gradient(180deg, var(--sky-top), var(--sky-bottom) 70%, #d9dde2);
  }
  .divider { position: absolute; left: 91px; top: 309px; width: 684px; height: 14px; }
  .overview { position: absolute; left: 91px; top: 340px; width: 680px; font-size: 15px; line-height: 20px; letter-spacing: 2.4px; }
  .overview p { margin-bottom: 16px; }
  .overview strong { font-weight: 700; }
  .overview__topics-title { margin-bottom: 6px; font-weight: 700; }
  .overview ul { list-style: none; padding-left: 54px; }
  .overview li { position: relative; margin-bottom: 2px; }
  .overview li::before {
    content: ""; position: absolute; left: -24px; top: 6px; width: 7px; height: 7px;
    border-radius: 50%; background: var(--orange);
  }
  .info-panel { position: absolute; left: 822px; top: 298px; width: 340px; height: 576px; }
  .info-panel__tab {
    position: absolute; z-index: 1; left: 0; top: 0; height: 26px; padding: 0 26px 0 14px;
    background: var(--tab); color: var(--paper); border-radius: 12px 12px 0 0;
    text-transform: none; font-size: 16px; font-weight: 600; line-height: 26px;
  }
  .info-panel__body {
    position: absolute; left: 0; top: 22px; width: 340px; height: 552px;
    background: linear-gradient(180deg, var(--panel-top), var(--panel-bottom));
    border: 1px solid var(--panel-edge); border-radius: 10px;
    box-shadow: 2px 3px 6px rgba(0,0,0,.3);
    padding: 34px 18px 0 30px; font-size: 18px; line-height: 23px; letter-spacing: 2px;
  }
  .info-panel__label { color: var(--orange); font-weight: 700; margin-bottom: 8px; }
  .info-panel__value { margin-bottom: 18px; font-weight: 700; }
  .info-panel__email { text-decoration: underline; }
  .info-panel__note { margin-top: 20px; text-align: center; font-size: 14px; line-height: 19px; letter-spacing: 1.5px; }
  .partners { position: absolute; top: 832px; left: 212px; display: flex; gap: 140px; align-items: center; }
  .partner-name { font-size: 22px; font-weight: 700; letter-spacing: 2px; color: var(--ink); }
  .partner-name--capital { color: var(--brand-navy); font-size: 17px; }
  .base-rule { position: absolute; left: 0; bottom: 4px; width: 1200px; height: 3px; background: var(--ink); }
</style>
</head>
<body>
<main class="flyer">
  <header class="masthead">
    <h1 class="masthead__title">Charting The Handover:</h1>
    <h2 class="masthead__subtitle">Securing and Growing Worth<br>Across An Ownership Shift</h2>
    <p class="masthead__audience">A complimentary breakfast seminar for owners and CEOs of private corporations with revenues ranging from $2M to $150M.</p>
    <p class="masthead__date">Thursday, February 24, 2011<br>7:45 – 10:00 AM</p>
  </header>

  <div class="hero-image" role="img" aria-label="Staircase rising into the sky toward an open doorway"></div>

  <svg class="divider" role="img" aria-label="Decorative scroll divider" viewBox="0 0 684 14">
    <rect x="0" y="5" width="684" height="4" fill="var(--rule-brown)" opacity=".7"/>
  </svg>

  <section class="overview">
    <p>Almost <strong>two-thirds of independent business owners</strong> in Canada are planning to exit their business within the next decade. The spoils will go to those who have planned in advance. Are you one of them?</p>
    <p>Join Marcus Hale, Partner at KTMW Chartered Accountants, and Devin Ostrow, co-founder of Meridel Capital Partners, for a compelling overview of one of the most critical issues affecting privately-held businesses today.</p>
    <p class="overview__topics-title">Topics of discussion will include:</p>
    <ul>
      <li>The alternatives for exiting a business and the implications of each</li>
      <li>Tax minimization strategies for the sale/transfer of your business</li>
      <li>Tactics for gaining control of the deal to achieve a successful sale and maximize the value you receive from it</li>
      <li>Real-life case studies and lessons to be learned from them</li>
    </ul>
  </section>

  <aside class="info-panel">
    <div class="info-panel__tab">Information</div>
    <div class="info-panel__body">
      <p class="info-panel__label">When:</p>
      <p class="info-panel__value">Thursday, February 24, 2011<br>7:45 – 10:00 AM</p>
      <p class="info-panel__label">Where:</p>
      <p class="info-panel__value">KTMW Chartered Accountants<br>1870 Bayview Avenue, Suite 305<br>Toronto</p>
      <p class="info-panel__label">RSVP:</p>
      <p class="info-panel__value">Contact Claire Dunmore at 416.555.0147 x 210 or <span class="info-panel__email">seminars@ktmwca.com</span></p>
      <p class="info-panel__note">Pre-registration is required!<br>Seats are limited and will be reserved on a first-come, first-served basis.</p>
    </div>
  </aside>

  <footer class="partners">
    <span class="partner-name">KTMW</span>
    <span class="partner-name partner-name--capital">Meridel Capital Partners</span>
  </footer>
  <div class="base-rule"></div>
</main>
</body>
</html>
```